Flyers

Modify Existing Flyer and create another for exterior company
Updates

Previous Brief has been updated- we want to update this existing one also

Target Market(s)

Exterior Remodeling Customers

Industry/Entity Type

Remodeling/Construction

```html
<!DOCTYPE html>
<html lang="en">
<head>
<meta charset="utf-8">
<title>Crestline Roofing and Exteriors Flyer</title>
<link href="https://fonts.googleapis.com/css2?family=Oswald:wght@500;600;700&family=Poppins:wght@400;600;700&display=swap" rel="stylesheet">
<style>
:root{
  --orange:#dd4b1a;
  --blue:#1565c8;
  --navy:#1f2a44;
  --ink:#2b2b2b;
  --paper:#f3f4f7;
  --bg:#e4e6ea;
  --sky-top:#8fb0d2;
  --sky-bottom:#dfe7ef;
  --roof:#5b626c;
  --dark:#1c1f26;
}
*{margin:0;padding:0;box-sizing:border-box}
html,body{width:1200px;height:1184px;overflow:hidden;background:var(--bg)}
body{font-family:'Poppins',sans-serif;color:var(--ink)}
.flyer{position:absolute;left:190px;top:12px;width:820px;height:1160px;background:var(--paper);overflow:hidden;box-shadow:0 6px 24px rgba(0,0,0,.12)}
.flyer-shapes{position:absolute;inset:0}
.logo-plate{position:absolute;left:0;top:40px;width:300px;height:150px}
.brand{position:absolute;left:30px;top:78px;color:var(--navy);font-weight:700;line-height:1.05}
.brand-name{font-size:34px;letter-spacing:1px;display:block}
.brand-sub{font-size:15px;letter-spacing:.5px;display:block;margin-top:6px}
.brand-mark{position:absolute;left:30px;top:58px;width:12px;height:12px;background:var(--navy)}
.call{position:absolute;right:36px;top:30px;text-align:right}
.call-label{font-family:'Oswald',sans-serif;font-weight:600;font-size:17px;color:var(--navy);letter-spacing:.3px}
.call-pill{display:flex;align-items:center;gap:10px;margin-top:6px;border:2px solid var(--blue);border-radius:30px;padding:3px 18px 3px 3px;background:rgba(255,255,255,.85)}
.call-icon{width:38px;height:38px;border-radius:50%;background:var(--blue);display:flex;align-items:center;justify-content:center}
.call-number{font-family:'Oswald',sans-serif;font-weight:700;font-size:32px;color:var(--orange)}
.hero-title{position:absolute;left:150px;top:458px;color:#fff;font-family:'Oswald',sans-serif;font-weight:600;line-height:1}
.hero-title .line1{font-size:38px;display:block}
.hero-title .line2{font-size:80px;font-weight:700;display:block;letter-spacing:1px;margin-top:-2px}
.hero-tag{position:absolute;left:578px;top:508px;width:180px;color:#fff;font-weight:600;font-size:10px;line-height:1.5;text-transform:uppercase}
.section{position:absolute}
.section h2{font-family:'Oswald',sans-serif;font-weight:600;font-size:27px;line-height:32px;color:var(--orange);margin-bottom:6px}
.section p{font-size:10.5px;line-height:1.5;color:#333}
.ticks{list-style:none;margin-top:12px}
.ticks li{position:relative;padding-left:22px;font-size:11px;font-weight:600;color:#222;margin-bottom:6px;line-height:1.3}
.ticks li::before{content:"";position:absolute;left:2px;top:1px;width:6px;height:10px;border:solid var(--orange);border-width:0 2px 2px 0;transform:rotate(40deg)}
.photo{position:absolute;border-radius:2px}
.roofing{left:40px;top:635px;width:370px}
.gutters{left:40px;top:875px;width:370px}
.siding{left:460px;top:600px;width:330px}
.soffit{left:460px;top:835px;width:330px}
.photo-tile{left:245px;top:770px;width:165px;height:95px;background:linear-gradient(150deg,#6c737c,#3b4048 60%,#9c8a70)}
.photo-gutter{left:245px;top:1000px;width:165px;height:75px;background:linear-gradient(180deg,#7fa6d4,#4c5158 55%,#d9dadb)}
.photo-siding{left:675px;top:728px;width:115px;height:90px;background:linear-gradient(160deg,#4c88cc,#8b9096 45%,#6f7a70)}
.photo-soffit{left:650px;top:960px;width:140px;height:80px;background:linear-gradient(170deg,#a6c4e6,#2f3337 40%,#eef0f2)}
.footer-url{position:absolute;left:40px;bottom:22px;display:flex;align-items:center;gap:12px;color:#fff;font-size:14px;letter-spacing:2px}
</style>
</head>
<body>
<div class="flyer">
  <svg class="flyer-shapes" width="820" height="1160" viewBox="0 0 820 1160">
    <defs>
      <linearGradient id="heroGrad" x1="0" y1="0" x2="0.6" y2="1">
        <stop offset="0" stop-color="var(--sky-bottom)"/>
        <stop offset="0.35" stop-color="var(--sky-top)"/>
        <stop offset="0.6" stop-color="var(--roof)"/>
        <stop offset="1" stop-color="#2e333a"/>
      </linearGradient>
    </defs>
    <g role="img" aria-label="Photo of a roofer installing standing seam metal roof panels under a cloudy sky">
      <polygon points="0,0 820,0 820,320 580,530 0,540" fill="url(#heroGrad)"/>
    </g>
    <polygon points="560,530 820,310 820,350 610,530" fill="var(--orange)"/>
    <polygon points="250,600 450,590 330,665" fill="var(--dark)"/>
    <polygon points="40,520 660,485 790,560 120,610" fill="var(--orange)"/>
    <polygon points="0,1105 500,1080 820,1010 820,1160 0,1160" fill="var(--blue)"/>
    <polygon points="0,1105 500,1080 820,1010 820,1020 500,1090 0,1115" fill="#ffffff" opacity=".6"/>
  </svg>

  <svg class="logo-plate" viewBox="0 0 300 150" aria-hidden="true"><polygon points="0,30 220,0 300,110 0,150" fill="#f3f4f7"/></svg>
  <div class="brand-mark"></div>
  <div class="brand"><span class="brand-name">CRESTLINE</span><span class="brand-sub">ROOFING AND EXTERIORS</span></div>

  <div class="call">
    <div class="call-label">CALL TODAY FOR YOUR FREE ESTIMATE</div>
    <div class="call-pill">
      <span class="call-icon"><svg width="20" height="20" viewBox="0 0 24 24"><path d="M6.6 10.8a15 15 0 0 0 6.6 6.6l2.2-2.2a1 1 0 0 1 1-.25 11.4 11.4 0 0 0 3.6.57 1 1 0 0 1 1 1V20a1 1 0 0 1-1 1A17 17 0 0 1 3 4a1 1 0 0 1 1-1h3.5a1 1 0 0 1 1 1c0 1.25.2 2.45.57 3.6a1 1 0 0 1-.25 1z" fill="#fff"/></svg></span>
      <span class="call-number">555-014-2287</span>
    </div>
  </div>

  <h1 class="hero-title"><span class="line1">ROOFING AND EXTERIOR</span><span class="line2">SPECIALIST</span></h1>
  <div class="hero-tag">Work with a top-rated<br>local remodeling<br>company in Cedar Ridge, IA</div>

  <section class="section roofing">
    <h2>ROOFING</h2>
    <p>When it comes to roofing, we install, site manage, and support your roof with 24/7 emergency roofing services. We are your local, family-owned roofing and home improvement specialists. No job is too big or too small. Our expert team is standing by to help answer your questions.</p>
    <ul class="ticks">
      <li>Asphalt Shingle Roof</li>
      <li>Tile Roof</li>
      <li>Metal Roof</li>
      <li>Residential or Commercial<br>Flat Roof</li>
    </ul>
  </section>
  <div class="photo photo-tile" role="img" aria-label="Photo of a dark tiled roof with a ridge cap"></div>

  <section class="section gutters">
    <h2>GUTTERS</h2>
    <p>Compliment or beautifully contrast your home exterior with leaf-guard gutters and rain-ware that lasts a lifetime. Roofing and Exteriors offers rain-ware that matches, complements or beautifully contrasts with your vinyl siding or color matches to your existing siding for a complete custom appearance.</p>
    <ul class="ticks">
      <li>Aluminum and stainless steel<br>materials</li>
      <li>Water running off</li>
      <li>Snap-Fit leaf guard system</li>
    </ul>
  </section>
  <div class="photo photo-gutter" role="img" aria-label="Photo of a tiled roof edge with a white gutter"></div>

  <section class="section siding">
    <h2>SIDING</h2>
    <p>Siding products, available in either cedar wood grain or smooth textures to beautify and protect your home. Enjoy decades of maintenance-free, stylish functionality that reflects your personality and improves your home's look and appeal. Home siding is now a 21st century products.</p>
    <ul class="ticks">
      <li>Advanced Durability</li>
      <li>A Bold First Impression</li>
      <li>Longer Lasting Beauty</li>
      <li>Realistic Woodgrain Textures</li>
    </ul>
  </section>
  <div class="photo photo-siding" role="img" aria-label="Photo of grey house siding and gables against a blue sky"></div>

  <section class="section soffit">
    <h2>SOFFIT/FASCIA</h2>
    <p>Soffit and fascia mentioned in the same breath. Together, this pair of roofing materials serves aesthetic and functional purposes. They cover unfinished structural parts of the roofline while protecting it from exposure to water, pests, and other potential damage.</p>
    <ul class="ticks">
      <li>Wood</li>
      <li>Vinyl</li>
      <li>Aluminum</li>
      <li>Composite</li>
    </ul>
  </section>
  <div class="photo photo-soffit" role="img" aria-label="Photo of a roof eave with labelled fascia board and soffit"></div>

  <div class="footer-url">
    <svg width="20" height="20" viewBox="0 0 24 24" fill="none" stroke="#fff" stroke-width="1.8"><circle cx="12" cy="12" r="10"/><path d="M2 12h20M12 2c3 3 3 17 0 20M12 2c-3 3-3 17 0 20"/></svg>
    <span>www.crestlineexteriors.com</span>
  </div>
</div>
</body>
</html>
```